Political themed graphic for contemporary church sermon series

Contemporary church in California need a graphic design for a sermon series. The sermon series will be focused on the upcoming presidential election. The sermon series is titled for the question "who will be the next president":

Title: 45
Subtitle: Who will it be / Does it matter

The design should use red, white and blue and should possibly have the cedar hall in the graphic somewhere. Maybe like a watermark or something to that effect.

Target Market(s)

Contemporary design,

Industry/Entity Type

Church

Font styles to use
Serif
Sans Serif

Colors
0555a3
ec1f27
ffffff

Requirements
Must have
• Political theme, red, white and blue (contemporary color palette). Cedar hall screened back in the design somewhere.
• the title large: 45
• and subtitle: Who will it be | Does it matter
Should not have
• I'm not looking for cheesy graphics with elephant and a donkey.

```html
<!DOCTYPE html>
<html lang="en">
<head>
<meta charset="utf-8">
<title>45 — Who Will It Be / Does It Matter</title>
<link rel="stylesheet" href="https://fonts.googleapis.com/css2?family=Saira+Extra+Condensed:wght@500;600&display=swap">
<style>
  :root {
    --page-bg: #e9e9ea;
    --card-bg: #ffffff;
    --ink-navy: #111925;
    --series-blue: #4a6b9c;
    --series-red: #c84a5d;
    --photo-red: #c4465a;
    --photo-grey: #b9b9b9;
    --photo-grey-deep: #2a2a2a;
    --photo-blue: #46679a;
  }
  * { margin: 0; padding: 0; box-sizing: border-box; }
  html, body {
    width: 1200px;
    height: 1000px;
    overflow: hidden;
    background: var(--page-bg);
  }
  .series-card {
    position: absolute;
    left: 290px;
    top: 135px;
    width: 658px;
    height: 688px;
    background: var(--card-bg);
    overflow: hidden;
  }
  .series-title {
    position: absolute;
    left: 0;
    top: 0;
    width: 658px;
    height: 270px;
    font-family: "Saira Extra Condensed", "Arial Narrow", sans-serif;
  }
  .series-number {
    font-size: 314px;
    font-weight: 600;
    fill: var(--ink-navy);
  }
  .series-subtitle {
    font-size: 108px;
    font-weight: 500;
    text-transform: uppercase;
  }
  .question-who { fill: var(--series-blue); }
  .question-matter { fill: var(--series-red); }
  .hall-photo {
    position: absolute;
    left: 0;
    top: 270px;
    width: 658px;
    height: 418px;
    background:
      linear-gradient(180deg, rgba(255,255,255,0) 35%, rgba(0,0,0,0.45) 100%),
      linear-gradient(90deg,
        var(--photo-red) 0%, var(--photo-red) 36%,
        var(--photo-grey) 42%, var(--photo-grey) 50%,
        var(--photo-blue) 56%, var(--photo-blue) 92%,
        var(--photo-grey-deep) 100%);
    clip-path: polygon(
      6% 10%, 9% 0%, 13% 6%, 18% 2%, 24% 9%, 30% 4%, 36% 12%,
      42% 20%, 50% 14%, 55% 8%, 60% 14%, 66% 4%, 72% 8%, 80% 2%,
      86% 10%, 92% 14%, 100% 16%, 100% 100%, 0% 100%, 0% 30%);
  }
</style>
</head>
<body>
  <main class="series-card">
    <svg class="series-title" viewBox="0 0 658 270" role="heading" aria-level="1" aria-label="45 — Who will it be, does it matter">
      <text class="series-number" x="13" y="245" textLength="187" lengthAdjust="spacingAndGlyphs">45</text>
      <text class="series-subtitle question-who" x="220" y="155" textLength="388" lengthAdjust="spacingAndGlyphs">WHO WILL IT BE</text>
      <text class="series-subtitle question-matter" x="220" y="245" textLength="427" lengthAdjust="spacingAndGlyphs">DOES IT MATTER</text>
    </svg>
    <div class="hall-photo" role="img" aria-label="Black and white photo of Cedar hall, washed with rough red and blue brush strokes"></div>
  </main>
</body>
</html>
```